Brisk Bookings needs a New Home page

We provide online appointment scheduling. There are many schedulers out there. Ours is unique because the scheduler is shown in one compact view that can be easily incorporated into the customer's website or Chatterbay page. Whether our customer is a solo hair-stylist or a large testing center with hundreds of testing seats at multiple locations, our customer still gets the same easy-to-use, one-page scheduling experience.

Our current home page, briskbookings.example, feels cluttered and outdated. We want something more modern and minimal.

Here are web pages we like:
artmosaic.example
tillquay.example
ruvel.example

We are not unhappy with the current logo or color scheme.

Need very clear call(s) to action (i.e. sign up for trial, schedule a demo).
Design needs to look good on devices of varying size.

Here are some ideas:
“Simple Online Scheduling” - Simple, compact design, easy-to-use & powerful, time-saving, chaos-taming, affordable, one page scheduling
“Stay in touch” - Basic email confirmations, reminders or targeted email notifications for follow-ups, no shows and more
“Multiple locations? No problem” - Schedule for multiple locations on one scheduler -
“Resource Pools” - Batting cages, clerks at the DMV, computers in a lab, pilates reformer machines
“Go Social” - Scheduling for Chatterbay and mobile devices
“Visual Reporting” - Reports
“Trusted” - Testimonials, reliable since 2005, etc.
List of industries (with links to industry-specific pages)

Ultimately want to redevelop the full site.
Updates

Reason: Please do not submit any new designs. We are now just wrapping up polling and discussing details. Thank you to all designers who have submitted. We feel lucky to get to chose from many great designs.

Target Market(s)

Audience is very broad including solo entrepreneurs (massage therapist, accountants, lawyers), educational institutions (elementary schools, university departments, advisers, testing centers), health care providers and screening services, to government.

Industry/Entity Type

Online

Requirements
Must have
• Call(s) to action, i.e. sign up for trial, schedule a demo.
• Look good on devices of different sizes.

```html
<!DOCTYPE html>
<html lang="en">
<head>
<meta charset="utf-8">
<title>Brisk Bookings – Simple Online One Page Scheduling</title>
<link rel="stylesheet" href="https://fonts.googleapis.com/css2?family=Raleway:wght@300;400;500;600&display=swap">
<style>
:root{
  --ink:#2b2b2b;
  --text:#555;
  --muted:#a9a9a9;
  --green:#8fbf1f;
  --red:#e14b3f;
  --teal:#19b5c0;
  --band:#f1f1f1;
  --dark-a:#333333;
  --dark-b:#2a2a2a;
  --footer:#272727;
  --white:#ffffff;
}
*{box-sizing:border-box;margin:0;padding:0}
html,body{width:1200px;height:2195px;overflow:hidden}
body{font-family:"Raleway",sans-serif;color:var(--text);background:var(--white);position:relative}
ul{list-style:none}
a{color:inherit;text-decoration:none}

/* header */
.site-header{position:absolute;top:0;left:0;width:1200px;height:70px;background:var(--white)}
.brand{position:absolute;left:140px;top:22px;display:flex;align-items:center;gap:8px;font-size:22px;font-weight:600;color:var(--ink)}
.brand-dot{width:12px;height:12px;border-radius:50%;background:var(--green)}
.cta{position:absolute;top:20px;height:32px;display:flex;align-items:center;justify-content:center;font-size:10px;font-weight:600;letter-spacing:.3px;border:2px solid #111}
.cta-trial{left:822px;width:116px;background:#111;color:var(--white)}
.cta-demo{left:942px;width:114px;background:var(--white);color:#111}

/* hero */
.hero{position:absolute;top:70px;left:0;width:1200px;height:396px;
  background:radial-gradient(ellipse at 75% 20%,#b98a45 0%,rgba(120,80,40,0) 45%),
             linear-gradient(100deg,#3a2616 0%,#6b4724 40%,#8a5e2f 65%,#4a3019 100%)}
.hero-title{position:absolute;left:139px;top:80px;font-size:31px;font-weight:300;line-height:38px;color:var(--white);letter-spacing:.5px}
.hero-steps{position:absolute;left:142px;top:180px;color:var(--white);font-size:12px;font-weight:500}
.hero-steps li{display:flex;align-items:center;gap:10px;height:23.5px}
.hero-steps .box{width:11px;height:11px;border:1.5px solid var(--white);display:inline-block}
.hero-steps .box.on{background:var(--white)}
.hero-shot{position:absolute;left:605px;top:95px;width:390px;height:301px;background:linear-gradient(180deg,#f4f4f4,#e2e2e2);border:1px solid #cfcfcf}
.hero-lens{position:absolute;left:598px;top:85px;width:190px;height:190px;border-radius:50%;background:#fafafa;box-shadow:0 4px 18px rgba(0,0,0,.35)}

/* nav */
.main-nav{position:absolute;top:466px;left:0;width:1200px;height:59px;border-bottom:1px solid #e6e6e6;display:flex;justify-content:center;align-items:center;gap:42px;font-size:11.5px;color:#444;font-weight:500}

/* why unique */
.unique-device{position:absolute;left:140px;top:600px;width:338px;height:436px;border-radius:18px;background:linear-gradient(160deg,#3d4247,#1f2327);box-shadow:0 12px 24px rgba(0,0,0,.18)}
.unique-title{position:absolute;left:610px;top:585px;font-size:40px;font-weight:300;color:#444;letter-spacing:1px}
.feature{position:absolute;left:610px;width:460px}
.feature-icon{position:absolute;left:0;top:0;width:52px;height:52px}
.feature h3{position:absolute;left:93px;top:0;font-size:16px;font-weight:400;color:#444}
.feature p{position:absolute;left:93px;top:24px;width:370px;font-size:11.5px;line-height:17px;color:var(--muted);font-weight:300}

/* stay in touch */
.touch{position:absolute;top:1116px;left:0;width:1200px;height:195px;background:var(--band)}
.touch-lead{position:absolute;left:0;top:0;width:490px;height:195px}
.touch h2{position:absolute;left:139px;top:42px;font-size:34px;font-weight:300;color:#444;letter-spacing:1px}
.touch-lead p{position:absolute;left:139px;top:104px;width:320px;font-size:11.5px;line-height:17px;color:var(--muted);font-weight:300}
.touch-item{position:absolute;top:42px;width:260px}
.touch-item svg{position:absolute;left:0;top:0}
.touch-item h3{position:absolute;left:62px;top:0;font-size:17px;font-weight:400;line-height:20px;color:#444}
.touch-item p{position:absolute;left:62px;top:58px;width:200px;font-size:11.5px;line-height:17px;color:var(--muted);font-weight:300}

/* resources & industries */
.split{position:absolute;top:1311px;height:293px;color:var(--white)}
.split-left{left:0;width:598px;background:var(--dark-a)}
.split-right{left:598px;width:602px;background:var(--dark-b)}
.split h2{position:absolute;top:44px;font-size:23px;font-weight:300;letter-spacing:.5px}
.split .rule{position:absolute;top:82px;width:235px;height:1px;background:#bbb}
.split p{position:absolute;top:98px;width:455px;font-size:11.5px;line-height:17px;font-weight:400}
.bullets{position:absolute;top:176px;font-size:10.5px;font-weight:600;letter-spacing:.3px}
.bullets li{height:24px;display:flex;align-items:center;gap:14px}
.bullets li::before{content:"";width:6px;height:6px;border-radius:50%;background:var(--white)}

/* social */
.social-title{position:absolute;left:139px;top:1655px;font-size:28px;font-weight:300;line-height:34px;color:#444;letter-spacing:.5px}
.social-text{position:absolute;left:139px;top:1755px;width:500px;font-size:11.5px;line-height:17px;color:var(--muted);font-weight:300}
.social-phone{position:absolute;left:800px;top:1640px;width:243px;height:244px;border-radius:26px 26px 0 0;background:linear-gradient(180deg,#3b3f44,#26292d)}
.social-screen{position:absolute;left:16px;top:72px;width:211px;height:172px;background:linear-gradient(180deg,#dfe6f2,#b6c8e3)}

/* testimonials */
.testimonials{position:absolute;top:1884px;left:0;width:1200px;height:256px;background:linear-gradient(180deg,#3d2a2d 0%,#4a3337 50%,#2f2426 100%);color:var(--white);text-align:center}
.testimonials h2{position:absolute;left:0;top:26px;width:1200px;font-size:27px;font-weight:300;letter-spacing:1px}
.quote{position:absolute;left:250px;top:78px;width:700px;font-size:11.5px;line-height:17px;font-weight:400}
.quote-name{position:absolute;left:0;top:136px;width:1200px;font-size:12px;font-weight:600;color:var(--teal)}
.slide-arrow{position:absolute;top:88px}
.quote-badge{position:absolute;left:572px;top:176px;width:56px;height:56px;border-radius:50%;background:var(--teal);display:flex;align-items:center;justify-content:center}

/* footer */
.site-footer{position:absolute;top:2140px;left:0;width:1200px;height:55px;background:var(--footer);font-size:10px;color:#8a8a8a}
.site-footer .copy{position:absolute;left:140px;top:21px}
.site-footer .legal{position:absolute;right:140px;top:21px}
</style>
</head>
<body>

<header class="site-header">
  <a class="brand" href="#"><span class="brand-dot"></span>Brisk Bookings</a>
  <a class="cta cta-trial" href="#">SIGN UP FOR TRIAL</a>
  <a class="cta cta-demo" href="#">SCHEDULE A DEMO</a>
</header>

<section class="hero" role="img" aria-label="Blurred warm-toned salon interior background">
  <h1 class="hero-title">SIMPLE ONLINE ONE PAGE<br>SCHEDULING</h1>
  <ul class="hero-steps">
    <li><span class="box on"></span>SELECT A DATE</li>
    <li><span class="box"></span>SELECT A SERVICE</li>
    <li><span class="box"></span>SELECT AN OPENING</li>
    <li><span class="box"></span>ENTER CONTACT INFORMATION</li>
    <li><span class="box"></span>CONFIRM APPOINTMENT</li>
  </ul>
  <div class="hero-shot" role="img" aria-label="Scheduler screen showing date calendar, service list and selected services"></div>
  <div class="hero-lens" role="img" aria-label="Magnified view of the date calendar"></div>
</section>

<nav class="main-nav">
  <a href="#">HOME</a><a href="#">SEE IT WORK</a><a href="#">WHO IT'S FOR</a><a href="#">OUR SCHEDULER</a><a href="#">FREE TRIAL</a><a href="#">DIG IN</a><a href="#">ABOUT US</a>
</nav>

<section class="unique">
  <div class="unique-device" role="img" aria-label="Tablet showing the home page with a magnified feature list"></div>
  <h2 class="unique-title">WHY ARE WE UNIQUE</h2>

  <div class="feature" style="top:688px">
    <svg class="feature-icon" viewBox="0 0 52 52" fill="none" stroke="var(--green)" stroke-width="2"><circle cx="26" cy="26" r="24"/><circle cx="26" cy="20" r="7"/><path d="M14 40c2-8 22-8 24 0"/></svg>
    <h3>EASY TO USE</h3>
    <p>Sed ut perspiciatis unde omnis iste natus error sit voluptatem accusantium doloremque laudantium, totam dicta sunt explicabo.</p>
  </div>
  <div class="feature" style="top:783px">
    <svg class="feature-icon" viewBox="0 0 52 52" fill="none" stroke="var(--green)" stroke-width="2"><circle cx="26" cy="26" r="24"/><circle cx="26" cy="26" r="14"/><path d="M26 17v9h7"/></svg>
    <h3>TIME SAVING</h3>
    <p>Sed ut perspiciatis unde omnis iste natus error sit voluptatem accusantium doloremque laudantium, totam dicta sunt explicabo.</p>
  </div>
  <div class="feature" style="top:878px">
    <svg class="feature-icon" viewBox="0 0 52 52" fill="none" stroke="var(--green)" stroke-width="2"><circle cx="26" cy="26" r="24"/><rect x="15" y="18" width="22" height="17"/><path d="M19 31l5-6 4 4 5-6"/></svg>
    <h3>AFFORDABLE</h3>
    <p>Sed ut perspiciatis unde omnis iste natus error sit voluptatem accusantium doloremque laudantium, totam dicta sunt explicabo.</p>
  </div>
  <div class="feature" style="top:973px">
    <svg class="feature-icon" viewBox="0 0 52 52" fill="none" stroke="var(--green)" stroke-width="2"><circle cx="26" cy="26" r="24"/><path d="M29 13l-10 15h8l-4 12 11-16h-8z"/></svg>
    <h3>POWERFUL</h3>
    <p>Sed ut perspiciatis unde omnis iste natus error sit voluptatem accusantium doloremque laudantium, totam dicta sunt explicabo.</p>
  </div>
</section>

<section class="touch">
  <svg class="touch-lead" viewBox="0 0 490 195" preserveAspectRatio="none"><path d="M0 0H440L490 97.5L440 195H0Z" fill="#f6f6f6"/></svg>
  <div class="touch-lead">
    <h2>STAY IN TOUCH</h2>
    <p>Lorem ipsum dolor sit amet, consectetur adipiscing elit, sed do eiusmod tempor incididunt ut labore et dolore magna ullamco laboris nisi ut aliquip.</p>
  </div>
  <div class="touch-item" style="left:520px">
    <svg width="36" height="30" viewBox="0 0 36 30" fill="none" stroke="var(--red)" stroke-width="2"><rect x="2" y="4" width="32" height="22"/><path d="M2 4l16 13 16-13"/></svg>
    <h3>BASIC EMAIL<br>CONFIRMATIONS</h3>
    <p>Lorem ipsum dolor sit amet, consectetur adipiscing elit, sed do aliquip ex ea commo</p>
  </div>
  <div class="touch-item" style="left:826px">
    <svg width="36" height="36" viewBox="0 0 36 36" fill="none" stroke="var(--red)" stroke-width="2"><path d="M18 4c-7 0-10 5-10 11v8l-4 5h28l-4-5v-8c0-6-3-11-10-11z"/><path d="M14 31a4 4 0 0 0 8 0"/></svg>
    <h3>TARGETED EMAIL<br>NOTIFICATIONS</h3>
    <p>Lorem ipsum dolor sit amet, consectetur adipiscing elit, sed do aliquip ex ea commo</p>
  </div>
</section>

<section class="split split-left">
  <h2 style="left:139px">OUR RESOURCE POOLS</h2>
  <div class="rule" style="left:139px"></div>
  <p style="left:139px">Lorem ipsum dolor sit amet, consectetur adipiscing elit, sed do eiusmod tempor incididunt ut labore et dolore magna ullamco laboris nisi ut aliquip ex ea commodo consequat.</p>
  <ul class="bullets" style="left:142px">
    <li>BATTING CAGES</li><li>CLERKS AT THE DMV</li><li>COMPUTERS IN A LAB</li><li>PILATES REFORMER MACHINES</li>
  </ul>
</section>
<section class="split split-right">
  <h2 style="left:45px">OUR INDUSTRIES</h2>
  <div class="rule" style="left:45px"></div>
  <p style="left:45px">Lorem ipsum dolor sit amet, consectetur adipiscing elit, sed do eiusmod tempor incididunt ut labore et dolore magna ullamco laboris nisi ut aliquip ex ea commodo consequat.</p>
  <ul class="bullets" style="left:48px">
    <li>ACCOUNTING</li><li>EDUCATION</li><li>HEALTH</li><li>WELLNESS</li>
  </ul>
  <ul class="bullets" style="left:182px">
    <li>MASSAGE</li><li>SALON</li><li>SPA</li><li>TAX</li>
  </ul>
</section>

<section class="social">
  <h2 class="social-title">NOW SCHEDULING...ON YOUR<br>CHATTERBAY PAGE</h2>
  <p class="social-text">At vero eos et accusamus et iusto odio dignissimos ducimus qui blanditiis praesentium voluptatum deleniti atque corrupti quos dolores et quas molestias excepturi sint occaecati cupiditate non provident, similique sunt in culpa qui officia deserunt mollitia animi, id est laborum et dolorum fuga. Et harum quidem rerum facilis est et expedita distinctio.</p>
  <div class="social-phone" role="img" aria-label="Phone showing the scheduler on a Chatterbay business page">
    <div class="social-screen"></div>
  </div>
</section>

<section class="testimonials" role="img" aria-label="Dim city skyline at dusk background">
  <h2>TESTIMONIALS</h2>
  <svg class="slide-arrow" style="left:195px" width="12" height="20" viewBox="0 0 12 20" fill="none" stroke="#ddd" stroke-width="1.5"><path d="M10 2L2 10l8 8"/></svg>
  <p class="quote">At vero eos et accusamus et iusto odio dignissimos ducimus qui blanditiis praesentium voluptatum deleniti atque corrupti quos dolores et quas molestias excepturi sint occaecati cupiditate non provident, similique sunt in culpa qui officia deserunt mollitia animi, id est laborum et dolorum fuga. Et harum quidem rerum facilis est et expedita distinctio.</p>
  <svg class="slide-arrow" style="left:940px" width="12" height="20" viewBox="0 0 12 20" fill="none" stroke="#ddd" stroke-width="1.5"><path d="M2 2l8 8-8 8"/></svg>
  <p class="quote-name">Sam Reader</p>
  <div class="quote-badge">
    <svg width="22" height="16" viewBox="0 0 22 16" fill="var(--white)"><path d="M0 16V9C0 4 2 1 7 0v3C4 4 4 6 4 8h4v8zM12 16V9c0-5 2-8 7-9v3c-3 1-3 3-3 5h4v8z"/></svg>
  </div>
</section>

<footer class="site-footer">
  <p class="copy">Copyright 2013 Brisk Bookings</p>
  <p class="legal">Copyright | Privacy and Billing Policies | Terms and Conditions</p>
</footer>

</body>
</html>
```